Clever & creative business card needed for a pediatric dentist.

We need a business card for a pediatric dentist that is building a brand-new pediatric dental practice. He is funny, outgoing, and sociable, and he hopes to give his business card to dentists and pediatricians so that he can give them information of where to refer infants, children, and teenagers that need high quality and attainable dental care.

The name of the dental practice is Copper Fern Pediatric Dentistry. Logo design .png / .pdf/ .jpg are provided to aid in the design.

The dentist's last name is Tolvan (which sounds like "burger", as in "hamburger” or “cheeseburger"). Since it is pediatric practice, kudos will be given to designs that implement a little joke into the design - but hopefully in a small or hidden way (such as putting something like a cheeseburger on the back of the card, or hiding it an an abstract way).

Thank you!

Please make a design that incorporates colors. It should be fun! Not too serious. It does not have to follow the color scheme of the logos.

```html
<!DOCTYPE html>
<html lang="en">
<head>
<meta charset="utf-8">
<title>Copper Fern Pediatric Dentistry – Business Card</title>
<link href="https://fonts.googleapis.com/css2?family=Montserrat:wght@400;500;700&display=swap" rel="stylesheet">
<style>
  :root {
    --backdrop: #d5d5d5;
    --card: #333333;
    --card-shade: #3a3a3a;
    --ink: #ffffff;
    --ink-soft: #e6e6e6;
    --green: #4fae6a;
    --green-dark: #3c9a58;
    --green-light: #a8dcb0;
    --rule: #cfcfcf;
  }
  * { box-sizing: border-box; margin: 0; padding: 0; }
  html, body { width: 1200px; height: 913px; overflow: hidden; }
  body {
    background: var(--backdrop);
    font-family: "Montserrat", sans-serif;
    position: relative;
  }
  .card {
    position: absolute;
    width: 560px;
    height: 320px;
    background: var(--card);
    overflow: hidden;
  }
  .card--front { left: 60px; top: 110px; }
  .card--back { left: 580px; top: 480px; }

  /* front */
  .brand {
    position: absolute;
    right: 40px;
    top: 36px;
    display: flex;
    align-items: center;
    gap: 12px;
    color: var(--ink);
  }
  .brand__dot {
    width: 40px; height: 40px; border-radius: 50%;
    background: var(--green-light);
  }
  .brand__name {
    font-weight: 500;
    font-size: 30px;
    line-height: 1;
    letter-spacing: 0.5px;
  }
  .brand__tag {
    display: block;
    font-weight: 500;
    font-size: 30px;
  }
  .brand__sub {
    display: block;
    font-size: 9px;
    letter-spacing: 3.2px;
    margin-top: 6px;
    font-weight: 500;
  }
  .divider {
    position: absolute;
    left: 300px; right: 30px; top: 152px;
    height: 1px;
    background: var(--rule);
  }
  .person {
    position: absolute;
    left: 36px;
    top: 120px;
  }
  .person__name {
    color: var(--green);
    font-weight: 700;
    font-size: 27px;
    letter-spacing: -0.5px;
    text-transform: uppercase;
  }
  .person__role {
    color: var(--ink-soft);
    font-size: 15px;
    margin-top: 2px;
  }
  .person__rule {
    width: 170px; height: 1px; background: var(--rule);
    margin: 12px 0 10px;
  }
  .contacts { list-style: none; }
  .contacts li {
    display: flex; align-items: center; gap: 10px;
    color: var(--ink-soft);
    font-size: 14px;
    line-height: 22px;
  }
  .contacts svg { width: 13px; height: 13px; flex: none; }
  .address {
    position: absolute;
    right: 40px;
    top: 172px;
    color: var(--ink-soft);
    font-size: 15px;
    line-height: 22px;
    text-align: left;
  }
  .band {
    position: absolute;
    left: 0; right: 0; bottom: 0;
    height: 10px;
    background: linear-gradient(90deg, var(--green-dark), var(--green) 55%, var(--green-light));
  }

  /* back */
  .back__motif {
    position: absolute;
    left: 110px; top: 30px;
    width: 340px; height: 260px;
    border-radius: 120px 120px 50px 50px;
    background: var(--card-shade);
  }
  .back__brand {
    position: absolute;
    left: 0; right: 0; top: 96px;
    display: flex; flex-direction: column; align-items: center;
    color: var(--ink);
  }
  .back__dot {
    width: 56px; height: 56px; border-radius: 50%;
    background: var(--green-light);
    margin-bottom: 14px;
  }
  .back__name {
    font-weight: 500;
    font-size: 44px;
    line-height: 1;
    letter-spacing: 0.5px;
  }
  .back__sub {
    font-size: 13px;
    letter-spacing: 5px;
    margin-top: 10px;
    font-weight: 500;
  }
</style>
</head>
<body>
  <section class="card card--front" aria-label="Business card front">
    <div class="brand">
      <span class="brand__dot"></span>
      <div>
        <span class="brand__tag">copper fern</span>
        <span class="brand__sub">PEDIATRIC DENTISTRY</span>
      </div>
    </div>

    <div class="divider"></div>

    <div class="person">
      <h1 class="person__name">Elliot Tolvan</h1>
      <p class="person__role">Managing Director</p>
      <div class="person__rule"></div>
      <ul class="contacts">
        <li>
          <svg viewBox="0 0 16 16" aria-hidden="true"><path fill="var(--green)" d="M3.6 1.5l2.3 2.9-1.4 1.6c.9 2 2.5 3.6 4.5 4.5l1.6-1.4 2.9 2.3-1.3 2.4C7 13.3 2.7 9 1.2 3z"/></svg>
          044-210 873 615
        </li>
        <li>
          <svg viewBox="0 0 16 16" aria-hidden="true"><rect x="1" y="3" width="14" height="10" fill="var(--green)"/><path d="M1 3l7 6 7-6" fill="none" stroke="var(--card)" stroke-width="1.3"/></svg>
          hello@copperfern.com
        </li>
        <li>
          <svg viewBox="0 0 16 16" aria-hidden="true"><circle cx="8" cy="8" r="7" fill="var(--green)"/><path d="M1 8h14M8 1c-3 3-3 11 0 14M8 1c3 3 3 11 0 14" fill="none" stroke="var(--card)" stroke-width="1"/></svg>
          www.copperfernsmiles.com
        </li>
      </ul>
    </div>

    <address class="address" style="font-style: normal;">
      58, Maple Court Lane<br>
      Brookside, 45190
    </address>

    <div class="band"></div>
  </section>

  <section class="card card--back" aria-label="Business card back">
    <div class="back__motif" role="img" aria-label="Faint outline illustration of a cheeseburger behind the practice name"></div>
    <div class="back__brand">
      <span class="back__dot"></span>
      <span class="back__name">copper fern</span>
      <span class="back__sub">PEDIATRIC DENTISTRY</span>
    </div>
  </section>
</body>
</html>
```